#28 - On the Letterheadpaper, can you please make the footercolorfields littlebit darker? I mean the Colors are too bright compared to the Logocolors, or?!
@Torven #22 - Can you please add on the backside the url's like on #7 ?
@quembrastudio #18 - Businesscard: The footer (colored fields) maybe a little bit to strong/high, can you test it with 2-3px less? #18 - Letterheadpaper: Need the footer (colored fields) here! Looks without ... nacked. ;) #18 - Please add the "Back of the business card"-things what you can read in the briefing.
@quembrastudio #1#2 - Eliminated; Better draft available with #4 #11 - Eliminated; I think the logo is better on a "normal" business card style, and maybe thats are other card Dimensions. #10 #9 - The Black Symbols on the Businesscard is maybe to strong. Can you test it with blue or grey symbols? #4 - At the moment my favorite, but please the "84116 Grunwiesel" in a new line under the Street (businesscard), thats the correct format in Germany. I'm not so happy with the URL in the blue footerfield, maybe smaller or in a other location, I don't know?! Please put on the letterhead the Facts from the footer into the header (right under the Logo), maybe in a small/tiny clear Fonttype. The Flyerbusinesscard don't have the color fields on the bottom?
@torven #8 - Front looks nice, but the Logo on the backside is not strong/"clear" enough I think. #7#5 - Eliminated; Not my Style, Sorry. #6 - Eliminated; The footer (blue field) on the Front was to heavy
Can't vote for your drafts the Flyer and Letterhead are missing.
@vOlpt
Nice blue symbols on the Businesscard, but the color on the backside is purple, I think that kills the blue/grey Logo and Style on the Frontside. And the Logo with Name under it is one unit, either the Logo with the Name direct under the Logo, or the Logo standalone. :)
Cant't vote for your drafts, don't need Envelopes but the Flyer. ;)
@Marble314
Thanks for your Drafts, but it's not my Style and I think it's not the Style from the Logo, the heavy yellow Background "kills" the nice look of the Blue/Grey Logo, too.
#2 In Germany is it more standard that the Logo is on the right side.
Please make a new draft with the Logo on the right side and the personal data (Address) under the Logo. In the footer comes the web address and maybe later some bank account informations or a funny quote.
I miss in the Address the ID and the Name of the City (I forget it in the briefing, Sorry) please add it to the drafts.
=> "84116 Grunwiesel"
The Name under the Logo ("Lukas Wendorf") looks like a little to big/wide on the right side, please let it start and end on the exact same width that the Logo is.
The "Background" of the Flyer with the integrated Business Card can't be complete blue, there will be some Text added in the future, it's a information Flyer with some facts about my work and so on, so there must be some space for these texts. The Businesscard "in" the Flyer must the same Card as the normal Business card, except the round corners.
The Dimensions from all the stuff is like the given Dimensions from the attached Information-PDF's?
OK, the price is guaranteed! I would upgrade this project, the Problem is I must pay with coinrelay, and in Germany you send via echeck the money from your regular bank account to coinrelay. But this way need very very long here on zentrofix.example (I don't know why), i paid this project on the 16. feb, today (25. fe) the project started, ~7 workdays for clearing the echeck. So, when I now pay the Guaranteed-Upgrade the project-option will confirmed when the project ends ...
The Logo itself comes from my first project here on zentrofix.example, and there was the price guaranteed, too.
#22 - Can you please add on the backside the url's like on #7 ?
@quembrastudio
#18 - Businesscard: The footer (colored fields) maybe a little bit to strong/high, can you test it with 2-3px less?
#18 - Letterheadpaper: Need the footer (colored fields) here! Looks without ... nacked. ;)
#18 - Please add the "Back of the business card"-things what you can read in the briefing.
#1 #2 - Eliminated; Better draft available with #4
#11 - Eliminated; I think the logo is better on a "normal" business card style, and maybe thats are other card Dimensions.
#10 #9 - The Black Symbols on the Businesscard is maybe to strong. Can you test it with blue or grey symbols?
#4 - At the moment my favorite, but please the "84116 Grunwiesel" in a new line under the Street (businesscard), thats the correct format in Germany. I'm not so happy with the URL in the blue footerfield, maybe smaller or in a other location, I don't know?! Please put on the letterhead the Facts from the footer into the header (right under the Logo), maybe in a small/tiny clear Fonttype. The Flyerbusinesscard don't have the color fields on the bottom?
@torven
#8 - Front looks nice, but the Logo on the backside is not strong/"clear" enough I think.
#7 #5 - Eliminated; Not my Style, Sorry.
#6 - Eliminated; The footer (blue field) on the Front was to heavy
So, trust me or not.
--- Gerold

```html
<!DOCTYPE html>
<html lang="de">
<head>
<meta charset="utf-8">
<title>Lukas Wendorf – Geschäftsausstattung</title>
<link href="https://fonts.googleapis.com/css2?family=Open+Sans:wght@400;700&display=swap" rel="stylesheet">
<style>
  :root {
    --stage: #e7e4df;
    --paper: #ffffff;
    --brand-blue: #1f5fbf;
    --brand-blue-light: #3c86e6;
    --band-blue-dark: #123f85;
    --band-blue: #1b56ad;
    --band-grey: #1f2024;
    --text: #3a3a3a;
    --text-soft: #6f6f6f;
    --window: #f4f5f7;
    --window-line: #b8bcc4;
  }
  * { box-sizing: border-box; margin: 0; padding: 0; }
  html, body { width: 1200px; height: 751px; overflow: hidden; }
  body {
    position: relative;
    background: var(--stage);
    font-family: "Open Sans", Arial, sans-serif;
    color: var(--text);
  }
  .sheet {
    position: absolute;
    background: var(--paper);
    box-shadow: 0 2px 8px rgba(0,0,0,.18);
  }
  .wordmark {
    font-weight: 700;
    color: var(--brand-blue);
    display: flex;
    align-items: center;
    gap: 6px;
    white-space: nowrap;
  }
  .wordmark .mark-square {
    width: 10px; height: 10px;
    background: var(--brand-blue);
  }

  /* Footer colour fields */
  .footer-bands { position: absolute; left: 0; right: 0; bottom: 0; height: 12px; display: flex; }
  .band-blue { flex: 1; background: linear-gradient(90deg, var(--band-blue-dark), var(--band-blue)); }
  .band-grey {
    width: 28%; background: var(--band-grey);
    color: #ccc; font-size: 6px; display: flex; align-items: center; justify-content: center;
  }

  /* Letterhead */
  .letterhead { left: 36px; top: 43px; width: 473px; height: 660px; }
  .letterhead .header { position: absolute; right: 30px; top: 30px; text-align: right; }
  .letterhead .header .wordmark { font-size: 17px; justify-content: flex-end; }
  .letterhead .header-facts {
    margin-top: 6px; font-size: 6px; line-height: 1.5; color: var(--text-soft); font-style: normal;
  }
  .letterhead .footer-line {
    position: absolute; left: 14px; bottom: 24px;
    font-size: 6.5px; color: var(--text-soft);
  }

  /* Business card front */
  .card-front { left: 403px; top: 197px; width: 298px; height: 175px; }
  .card-front .holder-name {
    position: absolute; left: 14px; top: 18px;
    font-size: 13px; font-weight: 700; color: var(--brand-blue);
  }
  .card-front .wordmark { position: absolute; right: 14px; top: 16px; font-size: 11px; }
  .card-front .contact {
    position: absolute; left: 150px; top: 50px;
    font-size: 7px; line-height: 1.45;
  }
  .card-front .contact dt { display: inline-block; width: 34px; }
  .card-front .contact dd { display: inline; }
  .card-front .footer-bands { height: 9px; }
  .card-front .band-blue {
    color: #fff; font-size: 5px; display: flex; align-items: center; padding-left: 28px;
  }

  /* Business card back */
  .card-back {
    left: 403px; top: 389px; width: 298px; height: 187px;
    background: linear-gradient(180deg, var(--brand-blue-light), var(--brand-blue) 70%, #164d9e);
    display: flex; align-items: center; justify-content: center;
  }
  .card-back .wordmark { color: #fff; font-size: 22px; }
  .card-back .wordmark .mark-square { background: #fff; width: 16px; height: 16px; }

  /* Envelopes */
  .envelope-window {
    position: absolute;
    border: 1px solid var(--window-line);
    border-radius: 12px;
    background: var(--window);
    display: flex; align-items: center; justify-content: center;
  }
  .envelope-small { left: 724px; top: 360px; width: 160px; height: 360px; }
  .envelope-small .envelope-window { left: 24px; top: 70px; width: 48px; height: 100px; }
  .envelope-small .wordmark { transform: rotate(90deg); font-size: 10px; }

  .envelope-long { left: 902px; top: 34px; width: 231px; height: 460px; }
  .envelope-long .envelope-window { left: 60px; top: 52px; width: 56px; height: 150px; }
  .envelope-long .sender {
    position: absolute; left: 128px; top: 56px;
    writing-mode: vertical-rl; font-size: 6px; line-height: 1.5; color: var(--text); font-style: normal;
  }
  .envelope-long .sender strong { color: var(--brand-blue); font-size: 7px; }
  .envelope-long .wordmark { transform: rotate(90deg); font-size: 10px; }
</style>
</head>
<body>

  <section class="sheet letterhead" aria-label="Briefbogen">
    <header class="header">
      <div class="wordmark"><span class="mark-square"></span>Lukas Wendorf</div>
      <address class="header-facts">
        Lindenweg 14<br>
        84116 Grunwiesel<br>
        Phone: 08841 / 2273150 · Cell: 0172 / 5508124<br>
        Fax: 08841 / 2273159 · mail@wendorf-lukas.example
      </address>
    </header>
    <p class="footer-line">Lindenweg 14 · 84116 Grunwiesel · Phone: 08841 / 2273150 · Cell: 0172 / 5508124 · Fax: 08841 / 2273159 · mail@wendorf-lukas.example</p>
    <div class="footer-bands">
      <div class="band-blue"></div>
      <div class="band-grey">www.wendorf-lukas.example</div>
    </div>
  </section>

  <section class="sheet card-front" aria-label="Visitenkarte Vorderseite">
    <h1 class="holder-name">Lukas Wendorf</h1>
    <div class="wordmark"><span class="mark-square"></span>Lukas Wendorf</div>
    <dl class="contact">
      <div>Lindenweg 14</div>
      <div>84116 Grunwiesel</div>
      <div><dt>Phone</dt><dd>: 08841 / 2273150</dd></div>
      <div><dt>Cell</dt><dd>: 0172 / 5508124</dd></div>
      <div><dt>Fax</dt><dd>: 08841 / 2273159</dd></div>
      <div><dt>Email</dt><dd>: mail@wendorf-lukas.example</dd></div>
    </dl>
    <div class="footer-bands">
      <div class="band-blue">www.wendorf-lukas.example</div>
      <div class="band-grey"></div>
    </div>
  </section>

  <section class="sheet card-back" aria-label="Visitenkarte Rückseite">
    <div class="wordmark"><span class="mark-square"></span>Lukas Wendorf</div>
  </section>

  <section class="sheet envelope-small" aria-label="Kuvert klein">
    <div class="envelope-window">
      <div class="wordmark">Lukas Wendorf</div>
    </div>
  </section>

  <section class="sheet envelope-long" aria-label="Kuvert DIN lang">
    <div class="envelope-window">
      <div class="wordmark">Lukas Wendorf</div>
    </div>
    <address class="sender">
      <strong>Lukas Wendorf</strong><br>
      Lindenweg 14<br>
      84116 Grunwiesel<br>
      Phone: 08841 / 2273150<br>
      mail@wendorf-lukas.example
    </address>
  </section>

</body>
</html>
```